Shiatsu & Massage Therapy

I need a business card designed for my Mobile Massage services. The client needs to know that I will be doing house calls.

Shiatsu is a japanese type of bodywork that utilizes the same concepts of acupuncture, with the belief that our vital life energy flows through energetic pathways in the body. I will also offer other massage services.

The business card itself I would like to have a design that is very crisp and not too cluttered. The design should be captivating and convey the message of a connection between the body and soul.

Target Market(s)

My target market are people that are already into holistic services and practices such as fitness, yoga, meditation.

Industry/Entity Type

Massage

Contact Information for Business Card

Corinne Halvaro LMT
6072319058
chalvaro@plumridge-mail.net

Font styles to use
Serif
Script

Colors
b7a5cc
fbf289
33a6d7
33b7a4

Requirements
Must have
• I love the look of the picture I attached, the one of the person meditating. I love how the background is very cosmic and stimulating. If there is any way to combine the graphic of the person massaging another person and that feeling of the other image that would be great. I love yellows, blues and purples. PLEASE do not use all of the images. I really would like a them to be inspiration for your own designs.

```html
<!DOCTYPE html>
<html lang="en">
<head>
<meta charset="utf-8">
<title>Meridian Touch – Mobile Massage Business Card</title>
<link rel="stylesheet" href="https://fonts.googleapis.com/css2?family=Open+Sans:wght@400;600;700&family=Cormorant+Garamond:wght@600;700&family=Great+Vibes&display=swap">
<style>
  :root {
    --ink: #111111;
    --frame: #0b0b0b;
    --accent: #e6ef00;
    --paper: #ffffff;
    --glow-core: #fffbea;
    --glow-mid: #f1e3b6;
    --glow-edge: #d9c48e;
    --lavender: #b7a5cc;
    --sun: #fbf289;
    --sky: #33a6d7;
    --teal: #33b7a4;
    --violet: #5b3f95;
    --text: #1a1a1a;
  }
  html, body {
    margin: 0;
    padding: 0;
    width: 995px;
    height: 1200px;
    overflow: hidden;
    background: var(--paper);
  }
  .canvas {
    position: relative;
    width: 995px;
    height: 1200px;
    font-family: "Open Sans", Arial, sans-serif;
    color: var(--text);
  }
  .card-art { position: absolute; left: 0; top: 0; }
  .card-frame { fill: var(--frame); }
  .corner-accent { fill: var(--accent); }
  .cut-line { stroke: var(--paper); stroke-width: 3; }
  .emblem-dot { fill: var(--ink); }
  .glow-core { stop-color: var(--glow-core); }
  .glow-mid { stop-color: var(--glow-mid); }
  .glow-edge { stop-color: var(--glow-edge); }
  .aura-violet { stop-color: var(--lavender); }
  .aura-clear { stop-color: var(--glow-mid); }
  .aura-sky { stop-color: var(--sky); }
  .aura-teal { stop-color: var(--teal); }

  .brand-name {
    position: absolute;
    margin: 0;
    font-family: "Open Sans", Arial, sans-serif;
    font-weight: 700;
    font-size: 29px;
    line-height: 36px;
    letter-spacing: 0.5px;
    color: var(--ink);
    white-space: nowrap;
    transform: translateX(-50%);
  }
  .brand-name--front { left: 236px; top: 222px; }
  .brand-name--back  { left: 517px; top: 925px; }

  .holder {
    position: absolute;
    left: 332px;
    top: 364px;
    width: 414px;
    text-align: center;
  }
  .holder-name {
    margin: 0;
    font-family: "Cormorant Garamond", Georgia, serif;
    font-weight: 700;
    font-size: 40px;
    line-height: 46px;
    color: var(--text);
    white-space: nowrap;
  }
  .holder-rule {
    height: 3px;
    background: var(--ink);
    margin-top: 4px;
  }
  .contacts {
    position: absolute;
    left: 340px;
    top: 428px;
    width: 400px;
    display: flex;
    justify-content: space-between;
    font-size: 16px;
    line-height: 24px;
    color: var(--text);
    white-space: nowrap;
  }
  .contact { display: flex; align-items: center; gap: 10px; }
  .contact svg { display: block; flex: none; }
  .icon-fill { fill: var(--ink); }
  .icon-line { fill: none; stroke: var(--ink); stroke-width: 1.6; }

  .tagline {
    position: absolute;
    margin: 0;
    left: 332px;
    top: 462px;
    width: 414px;
    text-align: center;
    font-family: "Great Vibes", "Brush Script MT", cursive;
    font-size: 30px;
    line-height: 40px;
    color: var(--violet);
    white-space: nowrap;
  }
  .tagline--back {
    left: 517px;
    top: 1018px;
    width: auto;
    transform: translateX(-50%);
    font-size: 28px;
  }
</style>
</head>
<body>
<div class="canvas">
  <svg class="card-art" width="995" height="1200" viewBox="0 0 750 905" xmlns="http://www.w3.org/2000/svg">
    <defs>
      <radialGradient id="cosmic-glow" cx="0.5" cy="0.28" r="0.8">
        <stop offset="0" class="glow-core"/>
        <stop offset="0.55" class="glow-mid"/>
        <stop offset="1" class="glow-edge"/>
      </radialGradient>
      <linearGradient id="cosmic-aura" x1="0" y1="0" x2="0.3" y2="1">
        <stop offset="0" class="aura-violet" stop-opacity="0.45"/>
        <stop offset="0.45" class="aura-clear" stop-opacity="0"/>
        <stop offset="0.8" class="aura-sky" stop-opacity="0.18"/>
        <stop offset="1" class="aura-teal" stop-opacity="0.32"/>
      </linearGradient>
    </defs>

    <g class="card card--front">
      <rect class="card-frame" x="40" y="30" width="670" height="400"/>
      <polygon class="corner-accent" points="565,30 710,30 710,170"/>
      <line class="cut-line" x1="553" y1="30" x2="710" y2="187"/>
      <rect class="cosmic-backdrop" x="75" y="62" width="597" height="335" fill="url(#cosmic-glow)"
            role="img" aria-label="Glowing cosmic backdrop with a meditating figure and light rays"/>
      <rect x="75" y="62" width="597" height="335" fill="url(#cosmic-aura)" aria-hidden="true"/>
      <polygon class="corner-accent" points="40,235 75,270 75,285 190,285 190,395 210,395 245,430 40,430"/>
      <line class="cut-line" x1="40" y1="221" x2="88" y2="269"/>
      <circle class="emblem-dot" cx="138" cy="330" r="40"/>
    </g>

    <g class="card card--back">
      <rect class="card-frame" x="40" y="460" width="670" height="400"/>
      <polygon class="corner-accent" points="565,460 710,460 710,605"/>
      <line class="cut-line" x1="553" y1="460" x2="710" y2="617"/>
      <rect class="cosmic-backdrop" x="75" y="493" width="597" height="334" fill="url(#cosmic-glow)"
            role="img" aria-label="Glowing cosmic backdrop with a meditating figure and light rays"/>
      <rect x="75" y="493" width="597" height="334" fill="url(#cosmic-aura)" aria-hidden="true"/>
      <polygon class="corner-accent" points="40,712 40,860 190,860"/>
      <line class="cut-line" x1="40" y1="700" x2="200" y2="860"/>
      <circle class="emblem-dot" cx="390" cy="745" r="12"/>
    </g>
  </svg>

  <p class="brand-name brand-name--front">MERIDIAN TOUCH</p>

  <div class="holder">
    <p class="holder-name">Corinne Halvaro LMT</p>
    <div class="holder-rule"></div>
  </div>

  <div class="contacts">
    <span class="contact contact--phone">
      <svg width="14" height="16" viewBox="0 0 14 16" aria-hidden="true">
        <path class="icon-fill" d="M2 1 h4 l1 4 -2 1.5 q1 3 3.5 4.5 l1.5 -2 4 1 v4 q-7 1 -11 -6 Q1 5 2 1 Z"/>
      </svg>
      +(607) 2319058
    </span>
    <span class="contact contact--email">
      <svg width="16" height="12" viewBox="0 0 16 12" aria-hidden="true">
        <rect class="icon-line" x="1" y="1" width="14" height="10"/>
        <path class="icon-line" d="M1 1 L8 7 L15 1"/>
      </svg>
      chalvaro@plumridge-mail.net
    </span>
  </div>

  <p class="tagline">Mobile Shiatsu &amp; Massage · House Calls</p>

  <p class="brand-name brand-name--back">MERIDIAN TOUCH</p>
  <p class="tagline tagline--back">We come to you</p>
</div>
</body>
</html>
```